Customer flyer

Hi there,

We need a flyer done for our father's business. It is called Tidal crest and the flyer will be distributed to realtors in British Columbia. He lends money to realtors when they have sold a home from the time subjects are removed from the transaction to when the sale closes. He is looking for a modern, classy look with the following information:

"Tidal Crest"

Realtor Pay Day upon Subject Removal

Did you know?

* Fees 100% tax deductable
* Same Day Service
* Confidential
* Low Rates

Your money from 738519 B.C. Ltd. and It can be directly deposited into your bank account or delivered to your office

For quote: call Gavin Merrow 250 555 0137

This is a small business so he doesn't have a logo and has never needed to do promotions before as it's run on word of mouth for the past 10 years. We are open to all ideas and suggestions - he is a finance guy so looking to you for the creative side :)

Thank you!

I don't like the phrase Realtor Pay Day upon subject removal. I think I prefer "Realtors! Celebrate Your Home sales upon subject removal" . Your thoughts?

Thank you

```html
<!DOCTYPE html>
<html lang="en">
<head>
<meta charset="utf-8">
<title>Tidal Crest – Realtor Pay Day</title>
<link rel="stylesheet" href="https://fonts.googleapis.com/css2?family=Roboto+Slab:wght@800&family=Arimo:wght@400;700&display=swap">
<style>
  :root {
    --backdrop: #6b4a2e;
    --green-light: #a9d94c;
    --green-mid: #7cbd33;
    --green-deep: #4f9420;
    --green-edge: #3c7a17;
    --band-top: #f9d84e;
    --band-bottom: #f0b925;
    --gold-top: #fff27a;
    --gold-bottom: #f2b51c;
    --text-yellow: #ffe45a;
    --text-cream: #fff8d6;
    --shadow: rgba(30, 60, 10, 0.75);
    --box-fill: rgba(255, 255, 255, 0.22);
  }
  * { margin: 0; padding: 0; box-sizing: border-box; }
  html, body {
    width: 1200px; height: 617px; overflow: hidden;
    background: var(--backdrop);
  }
  .flyer {
    position: absolute; left: 132px; top: 88px;
    width: 935px; height: 440px;
    background: linear-gradient(180deg, var(--green-mid) 0%, var(--green-deep) 100%);
    font-family: "Arimo", Arial, sans-serif;
    overflow: hidden;
  }
  .flyer__header-art { position: absolute; left: 0; top: 0; width: 935px; height: 170px; }
  .flyer__title {
    position: absolute; left: 0; right: 0; top: 8px;
    text-align: center;
    font-family: "Roboto Slab", Georgia, serif;
    font-weight: 800; font-size: 70px; letter-spacing: 3px; line-height: 1;
    background: linear-gradient(180deg, var(--gold-top) 10%, var(--gold-bottom) 85%);
    -webkit-background-clip: text; background-clip: text; color: transparent;
    filter: drop-shadow(2px 3px 2px var(--shadow));
  }
  .band {
    position: absolute; left: 0; top: 163px; width: 100%; height: 58px;
    background: linear-gradient(180deg, var(--band-top), var(--band-bottom));
    border-top: 3px solid var(--green-edge);
    border-bottom: 3px solid var(--green-edge);
    text-align: center;
  }
  .band__text {
    font-size: 40px; font-weight: 700; line-height: 52px;
    color: var(--text-yellow);
    text-shadow: 1px 2px 2px rgba(120, 90, 0, 0.7), 0 0 1px #b08700;
  }
  .info-box {
    position: absolute; top: 238px; height: 133px;
    background: var(--box-fill);
    border-radius: 4px;
    color: var(--text-yellow);
    font-weight: 700; font-size: 23px; line-height: 33px;
    text-shadow: 1px 1px 1px var(--shadow);
  }
  .info-box--about { left: 18px; width: 475px; padding: 2px 10px; }
  .info-box--perks { left: 540px; width: 389px; padding: 0 8px; top: 236px; }
  .perks { list-style: none; }
  .footer-rule {
    position: absolute; left: 0; top: 380px; width: 100%; height: 4px;
    border-top: 2px solid var(--green-edge);
    border-bottom: 1px solid rgba(255,255,255,0.25);
  }
  .contact {
    position: absolute; left: 0; right: 0; top: 390px;
    text-align: center;
    font-size: 34px; line-height: 44px;
    color: var(--text-yellow);
    text-shadow: 1px 2px 2px var(--shadow);
  }
  .contact__phone { font-weight: 700; }
</style>
</head>
<body>
  <main class="flyer">
    <svg class="flyer__header-art" viewBox="0 0 935 170" aria-hidden="false">
      <defs>
        <linearGradient id="header-fill" x1="0" y1="0" x2="0" y2="1">
          <stop offset="0" stop-color="#b5e055"/>
          <stop offset="1" stop-color="#8fcb3a"/>
        </linearGradient>
        <path id="tagline-arc" d="M 40 112 Q 467 150 895 96"/>
        <filter id="soft-shadow" x="-5%" y="-30%" width="110%" height="160%">
          <feDropShadow dx="1" dy="2" stdDeviation="1.2" flood-color="#2b520c" flood-opacity="0.8"/>
        </filter>
      </defs>
      <path d="M0 0 H935 V125 Q 470 165 0 140 Z" fill="url(#header-fill)"/>
      <path d="M0 140 Q 470 165 935 125" fill="none" stroke="#6aa82a" stroke-width="2"/>
      <text font-family="Arimo, Arial, sans-serif" font-size="35" font-weight="700"
            fill="#fff8d6" filter="url(#soft-shadow)" text-anchor="middle">
        <textPath href="#tagline-arc" startOffset="50%">Realtor Pay Day upon Subject Removal</textPath>
      </text>
    </svg>

    <h1 class="flyer__title">TIDAL CREST</h1>

    <div class="band"><p class="band__text">Did you know?</p></div>

    <section class="info-box info-box--about">
      <p>Your money from 738519 B.C. Ltd.<br>
      And it can be directly deposited<br>
      into your bank account or<br>
      delivered to your office.</p>
    </section>

    <section class="info-box info-box--perks">
      <ul class="perks">
        <li>* Fees 100% tax deductable</li>
        <li>* Same Day Service</li>
        <li>* Confidential</li>
        <li>* Low Rates</li>
      </ul>
    </section>

    <div class="footer-rule"></div>
    <p class="contact">For quote call Gavin Merrow: <span class="contact__phone">250 555 0137</span></p>
  </main>
</body>
</html>
```